Lindenfall Studio Business cards

Design our business cards and eventually a logo. The company is based in Paris, its activity is the retailing via internet of luxury home furniture (like Vantorelli, Bercasso, fradusi...) Our clients are international andwith a high sense of aesthetics. The design shall communicate wealth and trust with a high quality and aesthetic sense, pure lines Company Name is Lindenfall StudioExplanation of the name: usually people who wants to buy furniture usually go in a showroom. Today they go in showroom to test the furniture and they search for the price on internet, which is a "Lindenfall studio".We will not be a e-commerce site. Our site will be (another project) a presentation site which purpose is to reach qualified prospects. Then everything will be handled by phone, meeting etc.The business card must be professional as we will negotiate with many luxury brands, opportunity to represent them on our site, prices etc.As far as the color are concerned mostly black and whithe or grey. The font of the Lindenfall Studio name shall have some impact.

Target Market(s)

High-end furniture and buyers of luxury goods, international customers, mostly women who handle such projects.
We also deal with professional buyers (hotels as an example) and luxury brands

Contact Information for Business Card

standard format 85x55, lanscape card, square corners will be printed on thick high quality paper (300 or 350g)

Font styles to use
Sans Serif

Colors

Designer to choose colors to be used in the design.

Requirements
Must have
• Must be white, as the paper will be high quality, the paper will enhance the card.
• Name of the brand Lindenfall studio (with specific font which make it very nice looking and catch the attention. similar to Calibri or Calibri
• Name of person (will give you the name later (4 names and position)
• the position of the person
• Mobile phone, e-mail, Physical address 27, rue Caldenois, 75005 Paris, France (courrier only) our web site www.lindenfallstudio-example.fr
• The card must be simple and class
Nice to have
• Font of the address is smaller than the rest,
• Calibri font or similar on recto side with the name of the company which may look similar to the picture inserted in the brief.
• The grey color in the picture inserted is ok for us
Should not have
• Any parallel lines which represent the name of the company
• Any heavy design If you go on internet sites which present the furniture all designs are pure lines and high quality craftsmanship. To have an idea of our targetted client or brand we will be in touch: https://www.casavornetta-example.it/projects/
• Note that the picture added below is what we use, now as mail signature, up to you to have a better design etc.

```html
<!DOCTYPE html>
<html lang="fr">
<head>
<meta charset="utf-8">
<title>Lindenfall Studio – Business Cards</title>
<link rel="stylesheet" href="https://fonts.googleapis.com/css2?family=Jost:wght@300;400&display=swap">
<style>
  :root{
    --board:#c3c3c3;
    --shadow:#5b5858;
    --ink:#ffffff;
    --taupe:#9b8169;
    --stone:#5b5652;
    --onyx:#100f0f;
  }
  *{margin:0;padding:0;box-sizing:border-box}
  html,body{width:1141px;height:1200px;overflow:hidden}
  body{background:var(--board);position:relative;font-family:"Jost",sans-serif;color:var(--ink);font-weight:300}
  .card{position:absolute;width:497px;height:321px;background:var(--tone)}
  .card::before{content:"";position:absolute;left:-21px;top:16px;width:100%;height:100%;background:var(--shadow);filter:blur(5px);z-index:-1}
  .card--front{left:57px;border:1px solid var(--ink)}
  .card--back{left:606px}
  .row-1{top:52px}.row-2{top:440px}.row-3{top:827px}
  .tone-taupe{--tone:var(--taupe)}
  .tone-stone{--tone:var(--stone)}
  .tone-onyx{--tone:var(--onyx)}
  .brand{position:absolute;left:0;right:0;text-align:center;font-size:26px;letter-spacing:.3px;white-space:nowrap;line-height:1}
  .card--front .brand{top:33px}
  .card--back .brand{top:132px;font-size:27px}
  .person{position:absolute;left:49px;top:124px}
  .person__name{font-size:25px;line-height:1.1;letter-spacing:.2px}
  .person__role{font-size:11.5px;line-height:1.2;word-spacing:2px}
  .divider{position:absolute;left:247px;top:106px;width:1px;height:112px;background:var(--ink)}
  .contact{position:absolute;left:286px;top:122px;list-style:none;font-size:11.5px}
  .contact li{display:flex;align-items:flex-start;gap:8px;line-height:1.25}
  .contact li+li{margin-top:9px}
  .contact svg{width:9px;height:9px;flex:none;margin-top:3px;fill:var(--ink)}
  .contact .address{font-size:9.5px;margin-top:8px}
  .website{position:absolute;left:0;right:0;top:280px;text-align:center;font-size:11.5px}
</style>
</head>
<body>

<section class="card card--front tone-taupe row-1">
  <div class="brand">LINDENFALL STUDIO SAS</div>
  <div class="person"><div class="person__name">Maël Durocher</div><div class="person__role">President and Co-Founder</div></div>
  <div class="divider"></div>
  <ul class="contact">
    <li><svg viewBox="0 0 10 10"><path d="M2 9 C1 6 3 2 7 1 L8 2.5 L6 3.5 C4.5 4 3.5 6 4 8 Z"/></svg>+33614273958</li>
    <li><svg viewBox="0 0 10 10"><text x="0" y="8.5" font-size="10" font-family="Jost,sans-serif">@</text></svg>info@lfstudio-example.com</li>
    <li class="address"><svg viewBox="0 0 10 10"><path d="M5 1 L9.5 5 H8 V9 H6 V6.5 H4 V9 H2 V5 H.5 Z"/></svg><span>27, rue Caldenois,<br>75005 Paris, France</span></li>
  </ul>
  <div class="website">www.lindenfallstudio-example.fr</div>
</section>
<section class="card card--back tone-taupe row-1"><div class="brand">LINDENFALL STUDIO SAS</div></section>

<section class="card card--front tone-stone row-2">
  <div class="brand">LINDENFALL STUDIO SAS</div>
  <div class="person"><div class="person__name">Maël Durocher</div><div class="person__role">President and Co-Founder</div></div>
  <div class="divider"></div>
  <ul class="contact">
    <li><svg viewBox="0 0 10 10"><path d="M2 9 C1 6 3 2 7 1 L8 2.5 L6 3.5 C4.5 4 3.5 6 4 8 Z"/></svg>+33614273958</li>
    <li><svg viewBox="0 0 10 10"><text x="0" y="8.5" font-size="10" font-family="Jost,sans-serif">@</text></svg>info@lfstudio-example.com</li>
    <li class="address"><svg viewBox="0 0 10 10"><path d="M5 1 L9.5 5 H8 V9 H6 V6.5 H4 V9 H2 V5 H.5 Z"/></svg><span>27, rue Caldenois,<br>75005 Paris, France</span></li>
  </ul>
  <div class="website">www.lindenfallstudio-example.fr</div>
</section>
<section class="card card--back tone-stone row-2"><div class="brand">LINDENFALL STUDIO SAS</div></section>

<section class="card card--front tone-onyx row-3">
  <div class="brand">LINDENFALL STUDIO SAS</div>
  <div class="person"><div class="person__name">Maël Durocher</div><div class="person__role">President and Co-Founder</div></div>
  <div class="divider"></div>
  <ul class="contact">
    <li><svg viewBox="0 0 10 10"><path d="M2 9 C1 6 3 2 7 1 L8 2.5 L6 3.5 C4.5 4 3.5 6 4 8 Z"/></svg>+33614273958</li>
    <li><svg viewBox="0 0 10 10"><text x="0" y="8.5" font-size="10" font-family="Jost,sans-serif">@</text></svg>info@lfstudio-example.com</li>
    <li class="address"><svg viewBox="0 0 10 10"><path d="M5 1 L9.5 5 H8 V9 H6 V6.5 H4 V9 H2 V5 H.5 Z"/></svg><span>27, rue Caldenois,<br>75005 Paris, France</span></li>
  </ul>
  <div class="website">www.lindenfallstudio-example.fr</div>
</section>
<section class="card card--back tone-onyx row-3"><div class="brand">LINDENFALL STUDIO SAS</div></section>

</body>
</html>
```